Business Card Design

Company is a Commercial Building Company specialising in New Construction and existing refurbishments

Industry/Entity Type

Business

Contact Information for Business Card

Dale Mercer
Construction Manager
E Dale@harbridgebuilding.com.au
M 0400 213 947
Mail 27 Tarrant Rise Ridgehaven WA 6180

```html
<!DOCTYPE html>
<html lang="en">
<head>
<meta charset="utf-8">
<title>Harbridge Building &amp; Construction – Business Card</title>
<link href="https://fonts.googleapis.com/css2?family=Open+Sans:wght@400;600;700&display=swap" rel="stylesheet">
<style>
  :root {
    --cyan: #00b8d9;
    --orange: #f28a1e;
    --ink: #2f3338;
    --white: #ffffff;
    --stage: #e9ebed;
  }
  * { box-sizing: border-box; margin: 0; padding: 0; }
  html, body { width: 1200px; height: 1200px; overflow: hidden; }
  body {
    background: var(--stage);
    font-family: "Open Sans", Arial, sans-serif;
    position: relative;
  }
  .card {
    position: absolute;
    top: 225px;
    width: 460px;
    height: 750px;
    border-radius: 4px;
    overflow: hidden;
    box-shadow: 0 10px 30px rgba(0,0,0,0.15);
  }
  .card--front { left: 110px; background: var(--white); }
  .card--back { left: 630px; background: var(--cyan); }

  .brand {
    position: absolute;
    top: 90px;
    left: 0;
    right: 0;
    display: flex;
    flex-direction: column;
    align-items: center;
    gap: 22px;
  }
  .brand__square {
    width: 70px;
    height: 70px;
    border: 6px solid var(--cyan);
    border-radius: 10px;
  }
  .brand__name {
    font-weight: 600;
    color: var(--ink);
    text-transform: uppercase;
    text-align: center;
    font-size: 30px;
    line-height: 1.15;
    letter-spacing: 0.5px;
  }

  .contact-band { position: absolute; left: 0; top: 0; width: 460px; height: 750px; }

  .contact {
    position: absolute;
    left: 48px;
    top: 440px;
    color: var(--white);
    font-size: 21px;
    line-height: 1.5;
  }
  .contact__name { font-weight: 700; font-size: 27px; margin-bottom: 4px; }
  .contact__line { display: flex; align-items: center; gap: 12px; }
  .contact__line svg { width: 20px; height: 20px; flex: none; }
  .contact__gap { height: 10px; }

  .back-identity {
    position: absolute;
    inset: 0;
    display: flex;
    flex-direction: column;
    align-items: center;
    justify-content: center;
    color: var(--white);
    text-align: center;
  }
  .back-identity__name {
    font-weight: 600;
    text-transform: uppercase;
    font-size: 38px;
    line-height: 1.15;
    letter-spacing: 1px;
  }
  .back-identity__url {
    display: flex;
    align-items: center;
    gap: 12px;
    margin-top: 20px;
    font-size: 15px;
    letter-spacing: 4px;
  }
  .back-identity__rule { width: 36px; height: 2px; background: var(--white); }
</style>
</head>
<body>

<section class="card card--front">
  <div class="brand">
    <div class="brand__square"></div>
    <div class="brand__name">Harbridge Building<br>&amp; Construction</div>
  </div>

  <svg class="contact-band" viewBox="0 0 460 750" aria-hidden="true">
    <path d="M0 420 L400 290 Q460 270 460 330 L460 750 L0 750 Z" fill="var(--cyan)"/>
    <path d="M0 412 L398 283 Q466 260 466 330" fill="none" stroke="var(--orange)" stroke-width="7"/>
  </svg>

  <div class="contact">
    <div class="contact__name">Dale Mercer</div>
    <div>Construction Manager E</div>
    <div>Mail 27 Tarrant Rise</div>
    <div>Ridgehaven WA 6180</div>
    <div class="contact__gap"></div>
    <div class="contact__line">
      <svg viewBox="0 0 20 20"><rect x="5" y="1" width="10" height="18" rx="2" fill="none" stroke="#fff" stroke-width="2"/></svg>
      <span>0400 213 947</span>
    </div>
    <div class="contact__line">
      <svg viewBox="0 0 20 20"><rect x="1" y="4" width="18" height="12" fill="#fff"/><path d="M1 4 L10 11 L19 4" fill="none" stroke="var(--cyan)" stroke-width="1.6"/></svg>
      <span>Dale@harbridgebuilding.com.au</span>
    </div>
    <div class="contact__line">
      <svg viewBox="0 0 20 20"><circle cx="10" cy="10" r="8" fill="none" stroke="#fff" stroke-width="1.8"/><path d="M2 10 H18 M10 2 Q5 10 10 18 M10 2 Q15 10 10 18" fill="none" stroke="#fff" stroke-width="1.4"/></svg>
      <span>www.harbridgebuilding.com.au</span>
    </div>
  </div>
</section>

<section class="card card--back">
  <div class="back-identity">
    <div class="back-identity__name">Harbridge Building<br>&amp; Construction</div>
    <div class="back-identity__url">
      <span class="back-identity__rule"></span>
      <span>www.harbridgebuilding.com.au</span>
      <span class="back-identity__rule"></span>
    </div>
  </div>
</section>

</body>
</html>
```